Postcard Design

About Us

Lovely Lace and Lullabies is a Glamour kids Spa which is dedicated to making your princess’ day a dream come true. We specialize in the most glamorous spa parties in the Tri-State area. We create a memorable party for your child or children ages 17 and under. Whether it’s a Birthday Party, Sweet 16, Fundraiser, or maybe you just want to pamper your little princess for the day, we MAKE IT HAPPEN! You tell us the theme and we bring all the decorations and Spa items to you.

```html
<!DOCTYPE html>
<html lang="en">
<head>
<meta charset="utf-8">
<title>Lovely Lace and Lullabies – Postcard</title>
<link href="https://fonts.googleapis.com/css2?family=Yellowtail&family=Cabin+Condensed:wght@500;600;700&family=Baloo+2:wght@700;800&display=swap" rel="stylesheet">
<style>
  :root {
    --backdrop: #2c2b29;
    --gold: #c9a82c;
    --gold-line: #b8962a;
    --pink: #f06a8f;
    --pink-line: #f2a0b8;
    --white: #ffffff;
    --ink: #3a3a3a;
    --photo-dark: #1e170d;
    --photo-mid: #5a4420;
    --photo-warm: #8a6a2e;
  }
  * { margin: 0; padding: 0; box-sizing: border-box; }
  html, body { width: 1200px; height: 1200px; overflow: hidden; background: var(--backdrop); }
  .card { position: absolute; left: 250px; width: 702px; height: 545px; overflow: hidden; }
  .card--front { top: 42px; }
  .card--back { top: 614px; background: var(--white); }

  .photo {
    position: absolute; inset: 0;
    background:
      radial-gradient(ellipse at 30% 55%, #7a4f34 0%, rgba(122,79,52,0) 40%),
      radial-gradient(ellipse at 85% 10%, var(--photo-warm) 0%, rgba(138,106,46,0) 45%),
      linear-gradient(135deg, var(--photo-mid) 0%, var(--photo-dark) 60%, #120e08 100%);
  }
  .ribbon { position: absolute; left: 282px; top: 64px; width: 420px; height: 80px; }
  .ribbon__text {
    position: absolute; left: 318px; top: 72px;
    font-family: "Yellowtail", cursive; font-size: 42px; color: var(--white); line-height: 1;
  }
  .front__intro {
    position: absolute; left: 318px; top: 158px; width: 340px;
    font-family: "Cabin Condensed", sans-serif; font-weight: 600; font-size: 13.5px; line-height: 19px; color: var(--white);
  }
  .rule { position: absolute; left: 318px; width: 337px; height: 1.5px; }
  .rule--pink { top: 226px; background: var(--pink-line); }
  .rule--gold { top: 314px; background: var(--gold-line); }
  .front__headline {
    position: absolute; left: 318px; top: 233px; width: 360px;
    font-family: "Baloo 2", sans-serif; font-weight: 800; font-size: 22px; line-height: 24px;
    text-transform: uppercase; color: var(--white); letter-spacing: 0.3px;
  }
  .front__brand {
    position: absolute; left: 414px; top: 420px; width: 156px; text-align: center;
    font-family: "Cabin Condensed", sans-serif; font-weight: 700; font-size: 22px; line-height: 26px; color: var(--white);
  }

  .back__panel { position: absolute; left: 0; top: 0; width: 339px; height: 545px; background: var(--pink); }
  .back__intro {
    position: absolute; left: 29px; top: 30px; width: 300px;
    font-family: "Cabin Condensed", sans-serif; font-weight: 700; font-size: 16.5px; line-height: 22px; color: var(--white);
  }
  .back__banner { position: absolute; left: 0; top: 112px; width: 330px; height: 72px; }
  .back__banner-text {
    position: absolute; left: 28px; top: 124px;
    font-family: "Yellowtail", cursive; font-size: 36px; line-height: 1; color: var(--pink);
  }
  .back__body {
    position: absolute; left: 29px; top: 202px; width: 290px;
    font-family: "Cabin Condensed", sans-serif; font-weight: 600; font-size: 13.5px; line-height: 18.5px; color: var(--white);
  }
  .back__brand-box {
    position: absolute; left: 29px; top: 306px; width: 139px; height: 239px;
    background: var(--white); border: 2px solid var(--pink-line); border-bottom: none;
    display: flex; align-items: center; justify-content: center; text-align: center;
  }
  .back__brand-box span {
    font-family: "Cabin Condensed", sans-serif; font-weight: 500; font-size: 17px; line-height: 21px; color: var(--ink);
  }
  .contact { position: absolute; left: 176px; top: 326px; color: var(--white); font-family: "Cabin Condensed", sans-serif; }
  .contact__title { font-family: "Yellowtail", cursive; font-size: 32px; line-height: 1; margin-bottom: 10px; }
  .contact__row { display: flex; align-items: center; gap: 5px; }
  .contact__row--phone { font-weight: 700; font-size: 17px; margin-bottom: 6px; }
  .contact__row--small { font-weight: 500; font-size: 10px; margin-bottom: 8px; }
  .contact svg { flex: none; }
</style>
</head>
<body>

<section class="card card--front">
  <div class="photo" role="img" aria-label="Photo of a red-haired little girl in a floral dress among golden sunlit leaves, with pink spa party illustrations of a tiara, dress, perfume, shoes and mirror"></div>

  <svg class="ribbon" viewBox="0 0 420 80" aria-hidden="true">
    <polygon points="0,0 420,0 420,80 0,80 28,40" fill="var(--gold)"/>
    <polyline points="8,6 414,6" stroke="#e6cf6a" stroke-width="1.5" fill="none"/>
    <polyline points="8,74 414,74" stroke="#e6cf6a" stroke-width="1.5" fill="none"/>
  </svg>
  <div class="ribbon__text">We Make It Happen !</div>

  <p class="front__intro">Whether its a Birthday Party, Sweet 16, Fundraiser, or maybe you just want to pamper your little princess for the day</p>
  <div class="rule rule--pink"></div>
  <h2 class="front__headline">You tell us the theme and we bring all the decorations and spa items to you.</h2>
  <div class="rule rule--gold"></div>

  <div class="front__brand">Lovely Lace and Lullabies</div>
</section>

<section class="card card--back">
  <div class="back__panel"></div>
  <p class="back__intro">Lovely Lace and Lullabies is a Glamour kids Spa which is dedicated to making your Princess day a</p>

  <svg class="back__banner" viewBox="0 0 330 72" aria-hidden="true">
    <polygon points="0,0 330,0 306,36 330,72 0,72" fill="var(--white)"/>
    <polyline points="0,4 320,4 298,36 320,68 0,68" stroke="var(--pink-line)" stroke-width="1.5" fill="none"/>
  </svg>
  <div class="back__banner-text">Dream Come True.</div>

  <p class="back__body">We specialize in the most glamorous spa parties in the Tri-State area. We create a memorable party for your child or children ages 17 and under.</p>

  <div class="back__brand-box"><span>Lovely Lace and<br>Lullabies</span></div>

  <div class="contact">
    <div class="contact__title">Contact us</div>
    <div class="contact__row contact__row--phone">
      <svg width="9" height="14" viewBox="0 0 9 14"><rect x="0.75" y="0.75" width="7.5" height="12.5" rx="1.5" fill="none" stroke="#fff" stroke-width="1.5"/><rect x="3" y="10.5" width="3" height="1" fill="#fff"/></svg>
      <span>1234.456.789</span>
    </div>
    <div class="contact__row contact__row--small">
      <svg width="11" height="8" viewBox="0 0 11 8"><rect x="0.5" y="0.5" width="10" height="7" fill="none" stroke="#fff"/><polyline points="0.5,0.5 5.5,4.5 10.5,0.5" fill="none" stroke="#fff"/></svg>
      <span>hello@lacelullabies.com</span>
    </div>
    <div class="contact__row contact__row--small">
      <svg width="11" height="11" viewBox="0 0 11 11"><circle cx="5.5" cy="5.5" r="5" fill="none" stroke="#fff"/><ellipse cx="5.5" cy="5.5" rx="2.2" ry="5" fill="none" stroke="#fff"/><line x1="0.5" y1="5.5" x2="10.5" y2="5.5" stroke="#fff"/></svg>
      <span>www.lovelylacelullabies.com</span>
    </div>
  </div>
</section>

</body>
</html>
```